Harborview Behavioral and Community Services

Intellectual Developmental Disabilities, Group Homes, Residential Homes and Substance Abuse Residential facilities

Target Market(s)

Adults 18-59 male and female autism, developmental disabilities and mental health

Industry/Entity Type

Intellectual Development Disabilities, Autism, Applied Behavioral Analysis, Mental Health, Substance Abuse

Coding

Coded - Design and coding required

Number of Pages Required

5+ page

Font styles to use
Serif

Colors
0054AA
0677BA
7BADD7
CADEEF
E8F1F8

Requirements
Should not have
• Not specified

```html
<!DOCTYPE html>
<html lang="en">
<head>
<meta charset="utf-8">
<title>Harborview Behavioral and Community Services</title>
<link href="https://fonts.googleapis.com/css2?family=PT+Serif:wght@400;700&family=Open+Sans:wght@400;600;700&display=swap" rel="stylesheet">
<style>
:root{
  --navy:#0054AA;
  --blue:#0677BA;
  --sky:#7BADD7;
  --mist:#CADEEF;
  --ice:#E8F1F8;
  --ink:#1d2b3a;
  --white:#ffffff;
  --serif:'PT Serif', Georgia, serif;
  --sans:'Open Sans', Arial, sans-serif;
}
*{box-sizing:border-box;margin:0;padding:0}
html,body{width:1200px;height:4052px;overflow:hidden}
body{position:relative;background:var(--white);font-family:var(--sans);color:var(--ink)}
.abs{position:absolute}
.photo{position:absolute}

/* hero */
.hero{position:absolute;left:0;top:0;width:1200px;height:730px;overflow:hidden}
.hero-photo{left:0;top:0;width:1200px;height:730px;background:linear-gradient(100deg,#3f6fa8 0%,#7fa3cc 35%,#cfdbea 60%,#e9eef4 100%)}
.wordmark{font-family:var(--serif);font-weight:700;font-size:30px;line-height:1}
.brand{left:60px;top:30px;color:var(--white)}
.nav{right:60px;top:12px;display:flex;gap:24px;align-items:center;font-size:17px;color:var(--white);font-weight:600}
.nav .pill{background:var(--blue);padding:5px 16px;border-radius:16px}
.hero h1{left:60px;top:255px;color:var(--white);font-family:var(--serif);font-weight:700;font-size:58px;line-height:1.05}
.hero h1 span{display:block;font-size:34px;margin-top:6px}
.hero p{left:60px;top:372px;width:440px;color:var(--white);font-size:15px;line-height:1.45}
.btn{display:inline-block;background:var(--navy);color:var(--white);font-size:13px;font-weight:700;border-radius:22px;padding:12px 30px;letter-spacing:.5px}
.hero .btn{position:absolute;left:60px;top:480px}

/* section titles */
.title{position:absolute;font-family:var(--serif);font-weight:700;font-size:52px;color:var(--navy);display:flex;align-items:center;gap:16px}
.title .tag{background:var(--navy);color:var(--white);padding:0 18px;line-height:68px}

/* about */
.about-frame{left:138px;top:800px;width:340px;height:410px;border:4px solid var(--navy)}
.about-main{left:150px;top:812px;width:330px;height:390px;background:linear-gradient(135deg,#9db9d8,#e3ebf3)}
.about-inset{left:385px;top:975px;width:180px;height:235px;background:linear-gradient(160deg,#b9cfe4,#5f8fc2);border:6px solid var(--white)}
.badge{left:230px;top:826px;width:130px;height:78px;background:var(--blue);color:var(--white);font-size:17px;font-weight:600;padding:10px 10px 10px 46px;line-height:1.25}
.badge svg{position:absolute;left:12px;top:14px}
.about-text{left:660px;top:892px;width:460px;font-size:15px;line-height:1.5}
.about-list{left:670px;top:1010px;border-left:3px solid var(--sky);padding-left:16px;list-style:none;font-size:15px;line-height:2}
.about-list li{display:flex;align-items:center;gap:8px}
.about-btn{position:absolute;left:660px;top:1163px}

/* services */
.services{left:0;top:1300px;width:1200px;height:640px;background:var(--ice)}
.svc{position:absolute;width:240px;height:345px;background:var(--white);box-shadow:0 4px 14px rgba(0,60,120,.15);text-align:center}
.svc .pic{position:relative;height:150px;background:linear-gradient(135deg,#a8c3de,#e4ecf4)}
.svc .ico{position:absolute;left:96px;top:120px;width:48px;height:48px;border-radius:50%;background:var(--blue);display:flex;align-items:center;justify-content:center}
.svc p{margin:42px 18px 14px;font-size:14px;line-height:1.4;color:var(--navy)}
.svc .btn{padding:7px 22px;font-size:12px}

/* programs */
.prog{position:absolute;top:2160px;width:264px;height:290px;background:var(--white);box-shadow:0 4px 14px rgba(0,60,120,.15);text-align:center;border-bottom:8px solid var(--blue)}
.prog .pic{height:140px;background:linear-gradient(135deg,#8fb0d2,#dfe8f1)}
.prog h3{font-family:var(--serif);color:var(--navy);font-size:19px;margin:16px 10px 8px;line-height:1.15}
.prog p{font-size:13px;line-height:1.5;margin:0 22px}
.arrow{position:absolute;top:2500px;width:48px;height:48px;border-radius:50%;background:var(--sky);display:flex;align-items:center;justify-content:center}

/* contact */
.form{left:80px;top:2752px;width:660px;height:388px;background:var(--ice);box-shadow:0 4px 16px rgba(0,60,120,.18);padding:36px 40px}
.field{position:absolute;background:var(--mist);font-size:12px;font-weight:600;color:var(--ink);padding:10px 14px;height:36px}
.submit{position:absolute;left:225px;top:325px;width:210px;height:34px;background:var(--blue);color:var(--white);font-size:13px;font-weight:700;text-align:center;line-height:34px}
.follow{left:880px;top:2752px}
.follow h4{font-family:var(--serif);color:var(--navy);font-size:26px;letter-spacing:1px;margin:0 0 30px 40px}
.social{list-style:none}
.social li{display:flex;align-items:center;gap:18px;font-size:15px;margin-bottom:36px}
.social .dot{width:30px;height:30px;border-radius:50%;background:var(--navy)}

/* map */
.map{left:60px;top:3190px;width:1080px;height:430px;background:linear-gradient(135deg,#e6e9ec,#d6dadf);border:2px solid var(--mist)}

/* footer */
.footer{left:0;top:3700px;width:1200px;height:352px;background:var(--mist)}
.footer-brand{left:60px;top:3770px;color:var(--navy);font-size:28px}
.footer-about{left:60px;top:3835px;width:300px;font-size:14px;line-height:1.5}
.col{position:absolute;top:3760px;padding-left:20px;border-left:2px solid var(--sky);height:200px}
.col h5{font-family:var(--serif);color:var(--navy);font-size:20px;margin-bottom:22px}
.col ul{list-style:none;font-size:13px;line-height:2}
.copyright{left:0;top:4012px;width:1200px;height:40px;background:var(--navy);color:var(--white);font-size:14px;text-align:center;line-height:40px}
</style>
</head>
<body>

<header class="hero">
  <div class="photo hero-photo" role="img" aria-label="Caregiver smiling with an elderly woman in a wheelchair holding a cup of tea"></div>
  <div class="abs brand wordmark">Harborview</div>
  <nav class="abs nav"><span>Home</span><span>Report</span><span>About</span><span>Center</span><span class="pill">Contact Us</span></nav>
  <h1 class="abs">A Home Filled<span>with Care Respect &amp; Support</span></h1>
  <p class="abs">Lorem Ipsum Dolor Sit Amet Consectetur. Eget Mauris As Lacinia Pellentesque Magna. Nullam Diam Lio Aliquam Convallis. Vitae Eget Enim Irving Monper Rounhals Alio Bela The Mene.</p>
  <span class="btn">GET IN TOUCH</span>
</header>

<section class="about">
  <div class="abs about-frame"></div>
  <div class="photo about-main" role="img" aria-label="Carer supporting an older woman at home"></div>
  <div class="photo about-inset" role="img" aria-label="Staff member helping a resident walk"></div>
  <div class="abs badge">
    <svg width="26" height="26" viewBox="0 0 26 26"><circle cx="13" cy="13" r="11" fill="none" stroke="#fff" stroke-width="2"/><path d="M8 13l4 4 7-8" fill="none" stroke="#fff" stroke-width="2"/></svg>
    Continue be 30+ year
  </div>
  <h2 class="title" style="left:660px;top:796px"><span class="tag">About</span>US</h2>
  <p class="abs about-text">Lorem ipsum dolor sit amet consectetur. Eu parturient pellentesque auctor at pellentesque. Fringilla luctus aenean nec. Et eros lacinia feugiat lectus nec mentum nisi. Et vel volutpat.</p>
  <ul class="abs about-list">
    <li><svg width="14" height="14" viewBox="0 0 14 14"><path d="M2 7l3 3 7-7" fill="none" stroke="#0677BA" stroke-width="2"/></svg>Lorem ipsum dolor sit amet.</li>
    <li><svg width="14" height="14" viewBox="0 0 14 14"><path d="M2 7l3 3 7-7" fill="none" stroke="#0677BA" stroke-width="2"/></svg>Lorem ipsum dolor amet consectetur.</li>
    <li><svg width="14" height="14" viewBox="0 0 14 14"><path d="M2 7l3 3 7-7" fill="none" stroke="#0677BA" stroke-width="2"/></svg>Lorem ipsum dolor sit ame.</li>
  </ul>
  <span class="btn about-btn">DISCOVER MORE</span>
</section>

<section class="abs services">
  <h2 class="title" style="left:432px;top:40px;font-size:46px"><span style="color:var(--navy)">Our</span><span class="tag" style="line-height:60px">Service</span></h2>
  <article class="svc" style="left:60px;top:160px">
    <div class="pic" role="img" aria-label="Two residents sitting together"><span class="ico"><svg width="22" height="22" viewBox="0 0 22 22"><path d="M3 10l8-7 8 7v9H3z" fill="none" stroke="#fff" stroke-width="2"/></svg></span></div>
    <p>Safe and supportive living environments for independent growth.</p><span class="btn">Discover More</span>
  </article>
  <article class="svc" style="left:340px;top:268px">
    <div class="pic" role="img" aria-label="Carer assisting a man in a wheelchair"><span class="ico"><svg width="22" height="22" viewBox="0 0 22 22"><circle cx="11" cy="11" r="8" fill="none" stroke="#fff" stroke-width="2"/><path d="M11 6v5l3 3" stroke="#fff" stroke-width="2" fill="none"/></svg></span></div>
    <p>Always available assistance for emergencies and special needs.</p><span class="btn">Discover More</span>
  </article>
  <article class="svc" style="left:612px;top:160px">
    <div class="pic" role="img" aria-label="Counselling session with a resident"><span class="ico"><svg width="22" height="22" viewBox="0 0 22 22"><path d="M11 19s-8-5-8-10a4 4 0 018-1 4 4 0 018 1c0 5-8 10-8 10z" fill="none" stroke="#fff" stroke-width="2"/></svg></span></div>
    <p>Therapy and counseling to support emotional well-being.</p><span class="btn">Discover More</span>
  </article>
  <article class="svc" style="left:888px;top:268px">
    <div class="pic" role="img" aria-label="Carer chatting with an elderly woman"><span class="ico"><svg width="22" height="22" viewBox="0 0 22 22"><circle cx="8" cy="8" r="3" fill="none" stroke="#fff" stroke-width="2"/><circle cx="15" cy="8" r="3" fill="none" stroke="#fff" stroke-width="2"/><path d="M2 18c1-4 10-4 11 0M9 18c1-4 10-4 11 0" fill="none" stroke="#fff" stroke-width="2"/></svg></span></div>
    <p>Helping individuals develop daily living and social interaction skills.</p><span class="btn">Discover More</span>
  </article>
</section>

<section class="programs">
  <h2 class="title" style="left:290px;top:2016px;font-size:46px"><span class="tag" style="line-height:62px">Programs</span><span style="margin:0 20px">&amp;</span><span class="tag" style="line-height:62px">Facilities</span></h2>
  <article class="prog" style="left:168px"><div class="pic" role="img" aria-label="Residential apartment building"></div><h3>Residential Programs</h3><p>Lorem Ipsum Dolor . Egestis As Lacinia Pellen Eget Enim Ieng Monper</p></article>
  <article class="prog" style="left:466px"><div class="pic" role="img" aria-label="Carer supporting a resident with mental health care"></div><h3>Mental Health Support</h3><p>Lorem Ipsum Dolor . Egestis As Lacinia Pellen Eget Enim Ieng Monper</p></article>
  <article class="prog" style="left:770px"><div class="pic" role="img" aria-label="Group of residents gathered at a table"></div><h3>Community Integration Activities</h3><p>Lorem Ipsum Dolor . Egestis As Lacinia Pellen Eget Enim Ieng Monper</p></article>
  <span class="arrow" style="left:524px"><svg width="18" height="18" viewBox="0 0 18 18"><path d="M11 3L5 9l6 6" fill="none" stroke="#fff" stroke-width="3"/></svg></span>
  <span class="arrow" style="left:612px"><svg width="18" height="18" viewBox="0 0 18 18"><path d="M7 3l6 6-6 6" fill="none" stroke="#fff" stroke-width="3"/></svg></span>
</section>

<section class="contact">
  <h2 class="title" style="left:240px;top:2620px"><span class="tag">Content</span>US</h2>
  <form class="abs form">
    <span class="field" style="left:40px;top:38px;width:250px">NAME</span>
    <span class="field" style="left:350px;top:38px;width:250px">PHONE</span>
    <span class="field" style="left:40px;top:100px;width:250px">DD/MM/YY</span>
    <span class="field" style="left:350px;top:100px;width:250px">EMAIL</span>
    <span class="field" style="left:40px;top:162px;width:560px;height:130px">MESSAGE</span>
    <span class="submit">SUBMITE</span>
  </form>
  <div class="abs follow">
    <h4>FOLLOW US</h4>
    <ul class="social">
      <li><span class="dot"></span>Harborview Community Programs</li>
      <li><span class="dot"></span>Harborview Community Programs</li>
      <li><span class="dot"></span>Harborview Community Programs</li>
      <li><span class="dot"></span>Harborview Community Programs</li>
      <li><span class="dot"></span>Harborview Community Programs</li>
    </ul>
  </div>
</section>

<div class="abs map" role="img" aria-label="Street map showing the service location"></div>

<footer>
  <div class="abs footer"></div>
  <div class="abs footer-brand wordmark">Harborview</div>
  <p class="abs footer-about">Lorem Ipsum Dolor Sit Amet Consectetur. Eget Mauris As Lacinia Pellentesque Magna. Nullam Diam Lio Aliquam Convallis. Vitae Eget Enim Irving Monper</p>
  <div class="col" style="left:560px"><h5>Features</h5><ul><li>Lorem ipsum</li><li>Lorem ipsum</li><li>Lorem ipsum</li><li>Lorem ipsum</li></ul></div>
  <div class="col" style="left:740px"><h5>Connect</h5><ul><li>Lorem ipsum</li><li>Lorem ipsum</li><li>Lorem ipsum</li><li>Lorem ipsum</li></ul></div>
  <div class="col" style="left:910px"><h5>Terms of use</h5><ul><li>Lorem ipsum</li><li>Lorem ipsum</li><li>Lorem ipsum</li><li>Lorem ipsum</li></ul></div>
  <div class="abs copyright">Copyright (c) 2020 All rights reserved</div>
</footer>

</body>
</html>
```